The Fern Barrel Pub- restaurant menu, new launch

This is a new restaurant launching Summer 2017. Restaurant is a conversion of long standing small town existing family pizza/italian restaurant. new concept shifts concept to a family pub atmosphere featuring familiar appetizers, burgers, wood-fired pizza, and daily specials, draft beer, full- bar.

atmosphere is casual. want menu to reflect a more current "vibe" than the old place did. Not cold and modern, but retain the cozy familiar feel, without seeming dated and old fashioned.

4 panel menu; 8.5 X 11; 2-4 color
Updates

Project Deadline Extended
Reason: I am interested in seeing more designs. I will be providing feedback in the next few days on all designs submitted. I will also be increasing the budget.

Target Market(s)

Family-Oriented Pub, rural location Berkshire County, MA. Mostly Blue collar customer, value oriented

Industry/Entity Type

American Restaurant

Font styles to use
Sans Serif

Colors

Designer to choose colors to be used in the design.

Requirements
Must have
• Clear, uncluttered design, Highlighted items as specified in draft file (to come)
• ability to make changes daily as menu changes
• each panel separate sheet to slide into binder sleeve

```html
<!DOCTYPE html>
<html lang="en">
<head>
<meta charset="utf-8">
<title>The Fern Barrel Pub – Let's Get Started</title>
<link rel="stylesheet" href="https://fonts.googleapis.com/css2?family=Trocchi&family=Delius&family=Baloo+2:wght@700&family=Josefin+Sans:wght@300&display=swap">
<style>
  :root{
    --paper:#f7eee4;
    --red:#fa1e1b;
    --ink:#4f4848;
    --white:#ffffff;
  }
  *{margin:0;padding:0;box-sizing:border-box}
  html,body{width:927px;height:1200px;overflow:hidden;background:var(--paper)}
  .menu{position:relative;width:927px;height:1200px;background:var(--paper);color:var(--ink)}
  .abs{position:absolute}
  .serif{font-family:"Trocchi",Georgia,serif;font-weight:400;color:var(--ink);white-space:nowrap;font-variant-numeric:lining-nums}
  .hand{font-family:"Delius",sans-serif;color:var(--red);font-size:19px;line-height:30px;text-align:center;white-space:nowrap}
  .bold{font-family:"Baloo 2",sans-serif;font-weight:700;color:var(--red);font-size:21px;line-height:30px;text-align:center;letter-spacing:-.3px;white-space:nowrap}
  .rule{position:absolute;height:3px;background:var(--red)}
  .rule.ink{background:var(--ink)}

  .pub-name{left:86px;top:52px;font-size:58px;letter-spacing:-.5px}
  .section-tag{left:86px;top:136px;width:333px;height:48px;background:var(--red);color:var(--white);
    font-family:"Josefin Sans",sans-serif;font-weight:300;font-size:27px;letter-spacing:1.5px;line-height:52px;padding-left:28px}
  .tag-stripes{left:426px;top:136px}

  .divider{left:455px;top:234px;width:3px;height:360px;background:var(--red)}

  .dish-title{font-size:44px;text-align:center;letter-spacing:-1px}
  .wings{left:106px;width:292px}
  .chos{left:512px;width:300px}

  .boneless-box{left:113px;top:668px;width:295px;height:310px;border:3px solid var(--ink)}
  .boneless-title{left:113px;width:295px;top:678px;font-size:40px;line-height:52px;text-align:center;letter-spacing:-1.5px}
  .dip-box{left:510px;top:638px;width:306px;height:338px;background:var(--red)}
  .dip-title{left:536px;top:675px;color:var(--white);font-size:38px;line-height:50px;letter-spacing:-1.5px}
  .white{color:var(--white)}

  .salad-band{left:0;top:1026px}
  .salads-word{left:150px;top:1034px;font-size:52px;line-height:60px;letter-spacing:-1.5px}
  .salad-list{left:396px;top:1038px;font-family:"Delius",sans-serif;font-size:19px;line-height:30px;color:var(--ink);white-space:nowrap;letter-spacing:-.5px}
  .salad-list b{font-family:"Trocchi",serif;font-weight:400;font-variant-numeric:lining-nums}
</style>
</head>
<body>
<main class="menu">
  <h1 class="abs serif pub-name">The Fern Barrel Pub</h1>
  <div class="abs section-tag">LET'S GET STARTED</div>
  <svg class="abs tag-stripes" width="501" height="48" aria-hidden="true">
    <g fill="#fa1e1b">
      <rect x="0" y="0" width="501" height="4"/><rect x="0" y="9" width="501" height="4"/>
      <rect x="0" y="18" width="501" height="4"/><rect x="0" y="27" width="501" height="4"/>
      <rect x="0" y="36" width="501" height="4"/><rect x="0" y="44" width="501" height="4"/>
    </g>
  </svg>

  <h2 class="abs serif dish-title wings" style="top:226px">WINGS $12</h2>
  <p class="abs hand wings" style="top:293px">A Baker's Ten (that's 11) of<br>the biggest tastiest wings<br>you'll find anywhere.</p>
  <div class="rule" style="left:126px;top:393px;width:252px"></div>
  <p class="abs hand wings" style="top:402px">Choose from our<br>award-winning sauces:</p>
  <p class="abs bold wings" style="top:463px">buffalo mild, buffalo hot,<br>Rosie's Honey Chipolte,<br>Garlic Parm, BBQ,<br>Xtra Hot, Challenge Hot</p>
  <div class="rule" style="left:126px;top:602px;width:252px"></div>

  <div class="abs divider"></div>

  <h2 class="abs serif dish-title chos" style="top:224px">‘CHOS!! $11</h2>
  <div class="rule ink" style="left:530px;top:283px;width:264px"></div>
  <p class="abs hand chos" style="top:294px">Totchos and Nachos<br>and Cheese, oh my!</p>
  <p class="abs bold chos" style="top:359px">Add brisket $3<br>Add pulled pork $3<br>Add chili $3</p>

  <h2 class="abs serif dish-title chos" style="top:462px">Soup &amp; Stuff</h2>
  <div class="rule ink" style="left:530px;top:523px;width:264px"></div>
  <p class="abs bold chos" style="top:533px">Chowder $6<br>Chili $6<br>Du Jour $6</p>

  <div class="abs boneless-box"></div>
  <h2 class="abs serif boneless-title">BONELESS<br>“WINGS” $12</h2>
  <div class="rule ink" style="left:128px;top:792px;width:264px"></div>
  <div class="rule ink" style="left:128px;top:801px;width:264px"></div>
  <p class="abs hand" style="left:113px;width:295px;top:815px">Why are they called wings?<br>They're not wings. But it's<br>tasty boneless breaded chicken<br>anyway. Same great sauces,<br>8 “Wings.”</p>

  <div class="abs dip-box"></div>
  <div class="rule" style="left:534px;top:665px;width:264px;background:var(--white)"></div>
  <h2 class="abs serif dip-title">Spinach Arti-<br>choke Dip&nbsp; $10</h2>
  <div class="rule" style="left:534px;top:785px;width:264px;background:var(--white)"></div>
  <p class="abs hand white" style="left:510px;width:306px;top:801px">The good stuff.&nbsp; Real Spinach.<br>Real Artichokes, Real Cheese.<br>This did not come from a<br>bag.&nbsp; We make it right here,<br>every day.</p>

  <svg class="abs salad-band" width="816" height="76" aria-hidden="true">
    <g fill="#fa1e1b">
      <rect x="0" y="0" width="816" height="3"/>
      <rect x="0" y="8" width="139" height="4"/><rect x="0" y="17" width="139" height="4"/>
      <rect x="0" y="26" width="139" height="4"/><rect x="0" y="35" width="139" height="4"/>
      <rect x="0" y="44" width="139" height="4"/><rect x="0" y="53" width="139" height="4"/>
      <rect x="0" y="62" width="139" height="4"/>
      <rect x="139" y="73" width="677" height="3"/>
    </g>
  </svg>
  <h2 class="abs serif salads-word">SALADS</h2>
  <p class="abs salad-list">Fern Barrel Chopped Salad <b>$12</b> - Add chicken <b>$2</b><br>Gorgonzola Salad&nbsp; <b>$12</b> - Add chicken <b>$2</b></p>
</main>
</body>
</html>
```